International Company needs a Letterhead & Envelope Design

Our Company name is Brightfold Harbor Limited.
We'd like to ask the Designers for the luxurious and sophisticated design. Our logo is very simple and neat with letter logos, so we look forward to more professional and refined designs from Designers.
We look forward to providing you with a great design.
Thanks very much in advance.

```html
<!DOCTYPE html>
<html lang="en">
<head>
<meta charset="utf-8">
<title>Brightfold Harbor Limited — Letterhead</title>
<link href="https://fonts.googleapis.com/css2?family=Lato:wght@400;700;900&display=swap" rel="stylesheet">
<style>
  :root {
    --paper: #ffffff;
    --ink: #1e1e1e;
    --brand-grey: #555555;
    --watermark: #f3f3f3;
  }
  * { margin: 0; padding: 0; box-sizing: border-box; }
  html, body { width: 948px; height: 1200px; overflow: hidden; background: var(--paper); }
  .letterhead {
    position: relative;
    width: 948px; height: 1200px;
    background: var(--paper);
    font-family: "Lato", sans-serif;
    color: var(--ink);
    overflow: hidden;
  }
  .sender {
    position: absolute; top: 52px; right: 56px;
    width: 262px;
  }
  .sender__name {
    font-weight: 900; font-size: 19px; letter-spacing: 0.2px;
    color: var(--brand-grey); line-height: 1; margin-bottom: 22px; white-space: nowrap;
  }
  .sender__address, .sender__contact {
    font-size: 14px; line-height: 20px; letter-spacing: 0.4px; color: var(--ink);
  }
  .sender__contact { margin-top: 1px; line-height: 19px; }
  .sender__contact span { display: inline-block; width: 20px; }
  .letter {
    position: absolute; left: 56px; right: 56px; top: 236px;
    font-size: 17px; line-height: 30px;
  }
  .letter__date { margin-bottom: 34px; }
  .letter__recipient { line-height: 24.5px; margin-bottom: 72px; }
  .letter__greeting { margin-bottom: 12px; }
  .letter__body p { text-align: justify; margin-bottom: 25px; }
  .letter__closing { margin-top: 34px; }
  .signature { margin-top: 50px; }
  .signature__name { font-weight: 700; font-size: 21px; color: var(--brand-grey); line-height: 26px; }
  .signature__title { font-size: 17px; line-height: 24px; }
  .footer-mark {
    position: absolute; left: 40px; bottom: -42px;
    font-weight: 900; font-size: 150px; line-height: 1;
    color: var(--watermark); white-space: nowrap; letter-spacing: 4px;
  }
</style>
</head>
<body>
<main class="letterhead">
  <header class="sender">
    <div class="sender__name">Brightfold Harbor Limited</div>
    <div class="sender__address">418 Alder Quay Road,<br>Fenwick, OR 97201</div>
    <div class="sender__contact">
      <div><span>P</span>: 555.214.7380</div>
      <div><span>E</span>: hello@brightfoldharbor.com</div>
      <div><span>W</span>: www.brightfoldharbor.com</div>
    </div>
  </header>

  <article class="letter">
    <p class="letter__date">Date: 20 November 2018</p>
    <address class="letter__recipient" style="font-style:normal">
      To<br>
      Larkmeadow Gardens Ltd.<br>
      87 Willowmere Lane, Suite# B<br>
      Dunmore, UK 4300B12
    </address>
    <p class="letter__greeting">Dear Marsh,</p>
    <div class="letter__body">
      <p>Lorem Ipsum is simply dummy text of the printing and typesetting industry. Lorem Ipsum has been the industry's standard dummy text ever since the 1500s, when an unknown printer took a galley of type and scrambled it to make a type specimen book. It has survived not only five centuries, but also the leap into electronic typesetting, remaining essentially unchanged. It was popularised in the 1960s with the release of Transfer sheets containing Lorem Ipsum passages, and more recently with desktop publishing software like Folio Layout including versions of Lorem Ipsum.</p>
      <p>Lorem Ipsum is simply dummy text of the printing and typesetting industry. Lorem Ipsum has been the industry's.</p>
    </div>
    <p class="letter__closing">Thanking you</p>
    <div class="signature">
      <div class="signature__name">Alan Marsh</div>
      <div class="signature__title">CMCA</div>
    </div>
  </article>

  <div class="footer-mark" aria-hidden="true">BRIGHTFOLD</div>
</main>
</body>
</html>
```